A Must Standout Business Card Design

I need A card that stands out from the rest. Possibly raised letters or Metallic card, Shiny or glossy, Looking for a more modern look or something throwback design would be nice. So i'm a open to different designs. I have a logo but not to happy with it. I will send it on a sample business card I do like.I might like you to tweak the designed card I am sending you. A new logo may be in order too. Make logo something that can be engraved on metal. I was thinking possibly KR in a box or KR mirror image or Backward E then a forward B in a circle. The name of my company is KR Works Inc. I designed an innovative hand tool to remove Valve Cores. I call the tool the Stem Pin Clasp. My tool grips and holds onto valve cores like no other tool does. Check it out at my website stempinclasp.com Maybe put a picture of the tool on the card raised or embossed or that spot gloss.
Updates
Everybody I must say have sent over some awesome designs! Every submission has been my favorite so I will be making my decision after the deadline. Nice work everyone!
Target Market(s)
Automotive people, People who wholesale refrigeration parts and equipment, People who use tools
Industry/Entity Type
Business
Contact Information for Business Card
KR Works Inc., 4172 Larkfield Rd. Unit C Morris IL 60450, Doug Whitlow President, 708-555-0193, Stempinclasp.com, Logo
Look and feel
Each slider illustrates characteristics of the customer's brand and the style your logo design should communicate.

```html
<!DOCTYPE html>
<html lang="en">
<head>
<meta charset="utf-8">
<title>KR Works Inc – Business Card</title>
<link href="https://fonts.googleapis.com/css2?family=Source+Sans+3:wght@400;600;700&display=swap" rel="stylesheet">
<style>
  :root {
    --navy: #07497a;
    --red: #e6222b;
    --white: #ffffff;
    --steel-light: #e4e6e8;
    --steel-mid: #a9adb1;
    --steel-dark: #6f7478;
  }
  * { margin: 0; padding: 0; box-sizing: border-box; }
  html, body { width: 1200px; height: 702px; overflow: hidden; background: var(--white); }
  .card {
    position: relative;
    width: 1200px;
    height: 702px;
    background: var(--white);
    font-family: "Source Sans 3", "Myriad Pro", Arial, sans-serif;
    overflow: hidden;
  }
  .card p, .card h1 { line-height: 1; white-space: nowrap; }
  .brand-mark {
    position: absolute;
    left: 97px; top: 46px;
    width: 284px; height: 284px;
    border: 7px solid var(--navy);
    border-radius: 50%;
    display: flex; align-items: center; justify-content: center;
    background: var(--white);
    z-index: 2;
  }
  .brand-name {
    color: var(--navy);
    font-weight: 700;
    font-size: 46px;
    line-height: 1.05;
    text-align: center;
  }
  .tool-visual {
    position: absolute;
    left: 345px; top: 105px;
    width: 778px; height: 134px;
  }
  .holder-name {
    position: absolute;
    left: 0; width: 1200px;
    top: 319px;
    text-align: center;
    color: var(--red);
    font-size: 57px;
    font-weight: 400;
    padding-left: 12px;
  }
  .info-band {
    position: absolute;
    left: 0; top: 382px;
    width: 1200px; height: 320px;
    background: var(--navy);
    color: var(--white);
  }
  .holder-title {
    position: absolute;
    left: 0; width: 1200px;
    top: 15px;
    text-align: center;
    font-size: 44px;
    padding-left: 0;
  }
  .phone {
    position: absolute;
    left: 103px; top: 100px;
    font-size: 57px;
  }
  .website {
    position: absolute;
    left: 660px; top: 100px;
    font-size: 57px;
  }
  .address {
    position: absolute;
    left: 0; width: 1200px;
    top: 207px;
    text-align: center;
    font-size: 47px;
    padding-left: 4px;
  }
</style>
</head>
<body>
<main class="card">
  <div class="brand-mark">
    <span class="brand-name">KR Works<br>Inc</span>
  </div>

  <svg class="tool-visual" viewBox="0 0 778 134" role="img" aria-label="Photo of the Stem Pin Clasp hand tool with a valve core beside its tip">
    <defs>
      <linearGradient id="steel" x1="0" y1="0" x2="0" y2="1">
        <stop offset="0" stop-color="#e4e6e8"/>
        <stop offset="0.5" stop-color="#a9adb1"/>
        <stop offset="1" stop-color="#6f7478"/>
      </linearGradient>
    </defs>
    <rect x="0" y="0" width="778" height="134" rx="10" fill="url(#steel)" opacity="0.85"/>
  </svg>

  <h1 class="holder-name">Doug Whitlow</h1>

  <section class="info-band">
    <p class="holder-title">President</p>
    <p class="phone">708-555-0193</p>
    <p class="website">Stempinclasp.com</p>
    <p class="address">4172 Larkfield Rd., Unit C Dunmore OH 43917</p>
  </section>
</main>
</body>
</html>
```